Aunt Rolina's Bakery

I am about to create a luxury boutique that specializes in cake baking and cupcake
and ready for parties and special events and order delivery
the logo has already made

Industry/Entity Type

Boutique

Contact Information for Business Card

Email:auntrolinasbakery@maplecrumbmail.com
Instagram: aunt_rolina_bakery
Twitter: xxxxxxx
WhatsApp: xxxxxxx

Requirements
Must have
• luxury design

```html
<!DOCTYPE html>
<html lang="en">
<head>
<meta charset="utf-8">
<title>Aunt Rolina's Bakery – Business Card</title>
<link rel="stylesheet" href="https://fonts.googleapis.com/css2?family=Open+Sans:wght@400;600&display=swap">
<style>
  :root {
    --stage: #464646;
    --card-white: #f6f6f6;
    --rose: #d494a4;
    --taupe: #74716a;
    --ink-light: #ffffff;
  }
  * { box-sizing: border-box; margin: 0; padding: 0; }
  html, body { width: 1200px; height: 750px; overflow: hidden; }
  body {
    background: var(--stage);
    font-family: "Open Sans", sans-serif;
    position: relative;
  }
  .card {
    position: absolute;
    top: 228px;
    width: 461px;
    height: 262px;
    border-radius: 12px;
    overflow: hidden;
  }
  .card-front { left: 124px; background: var(--card-white); }
  .card-back { left: 618px; background: var(--rose); }

  .front-arc { position: absolute; left: 0; top: 0; }

  .contact-block {
    position: absolute;
    left: 22px;
    top: 119px;
    color: var(--ink-light);
  }
  .person-name { font-size: 16px; font-weight: 600; line-height: 20px; }
  .person-title { font-size: 12px; font-weight: 400; line-height: 16px; margin-bottom: 6px; }
  .contact-list { list-style: none; }
  .contact-item {
    display: flex;
    align-items: center;
    height: 17.6px;
    font-size: 9.5px;
    letter-spacing: -0.1px;
    white-space: nowrap;
  }
  .contact-icon {
    width: 12px; height: 12px;
    margin: 0 8px 0 2px;
    flex: none;
  }
  .social-dot {
    width: 10px; height: 10px;
    border: 1.5px solid var(--ink-light);
    border-radius: 50%;
    margin: 0 9px 0 3px;
    flex: none;
  }

  .brand-lockup {
    position: absolute;
    left: 283px;
    top: 22px;
    width: 160px;
    text-align: center;
    color: var(--taupe);
  }
  .brand-dot {
    width: 44px; height: 44px;
    border-radius: 50%;
    background: var(--rose);
    margin: 0 auto 10px;
  }
  .brand-name {
    font-size: 19px;
    font-weight: 400;
    line-height: 24px;
  }

  .back-mark {
    position: absolute;
    left: 167px;
    top: 66px;
    width: 128px;
    height: 128px;
    border: 4px solid var(--taupe);
    border-radius: 50%;
    display: flex;
    align-items: center;
    justify-content: center;
    text-align: center;
    color: var(--taupe);
    font-size: 15px;
    font-weight: 400;
    line-height: 19px;
  }
  .web-address {
    position: absolute;
    left: 0; right: 0;
    top: 226px;
    text-align: center;
    font-size: 11px;
    letter-spacing: 1px;
    color: var(--taupe);
  }
</style>
</head>
<body>
  <section class="card card-front">
    <svg class="front-arc" width="461" height="262" viewBox="0 0 461 262" aria-hidden="true">
      <circle cx="96" cy="222" r="158" fill="none" stroke="var(--taupe)" stroke-width="4"/>
      <circle cx="96" cy="222" r="154" fill="var(--rose)"/>
    </svg>

    <div class="contact-block">
      <p class="person-name">Mara Ellison</p>
      <p class="person-title">CEO/Founder</p>
      <ul class="contact-list">
        <li class="contact-item">
          <svg class="contact-icon" viewBox="0 0 12 12" aria-hidden="true"><path d="M2.5 1 L4.5 1 L5.3 3.4 L4 4.4 C4.6 5.9 6.1 7.4 7.6 8 L8.6 6.7 L11 7.5 L11 9.5 C11 10.4 10.3 11 9.4 11 C5 10.6 1.4 7 1 2.6 C1 1.7 1.6 1 2.5 1 Z" fill="var(--ink-light)"/></svg>
          555 201 7784
        </li>
        <li class="contact-item">
          <svg class="contact-icon" viewBox="0 0 12 12" aria-hidden="true"><rect x="1" y="2.5" width="10" height="7" fill="var(--ink-light)"/><path d="M1 2.5 L6 6.5 L11 2.5" fill="none" stroke="var(--rose)" stroke-width="1"/></svg>
          auntrolinasbakery@maplecrumbmail.com
        </li>
        <li class="contact-item"><span class="social-dot"></span>aunt_rolina_bakery</li>
        <li class="contact-item"><span class="social-dot"></span>auntrolinasbakery</li>
        <li class="contact-item"><span class="social-dot"></span>auntrolinasbakery</li>
      </ul>
    </div>

    <div class="brand-lockup">
      <div class="brand-dot"></div>
      <p class="brand-name">Aunt Rolina's<br>Bakery</p>
    </div>
  </section>

  <section class="card card-back">
    <div class="back-mark">Aunt Rolina's<br>Bakery</div>
    <p class="web-address">www.maplecrumbbakes.com</p>
  </section>
</body>
</html>
```